Norwegian psychologist service needs a fresh and exiting web site*

Norwegian psychologist service: working with therapy, personal development, mastery and personal growth. Focus: children and teenagers with special needs; family dynamics; group processes; individuals with a need for therapy and personal growth. (Our company name: Fjordlys og samhold (means Mastery and Growth).

We already have a logo for the company, which will be used (will be attached in the project).

The webside is to be structured in 4 pages with roll down curtain menus (the numbers are just for guiding the designer - the should not be added):

Page 1: Om Fjordlys og Samhold (about Mastery and Growth): this is where our business is is presented/described shortly: Lorem Ipsum dolor cit...

Page 2: Tjenester (Services): this is where our 5 service areas are presented:
2.1 Utredning (Investigation, diagnosing): Lorem Ipsum dolor cit...
2.2 Rådgivning (consulting): Lorem Ipsum dolor cit...

2.3 Kurs og work shops (courses and work shops): Lorem Ipsum dolor cit...
2.3a Fjordlys og samhold Tema 1 (T1)
2.3b Fjordlys og samhold Tema 2 (T2)
2.3c Fjordlys og samhold Tema 3 (T3)

2.4 Terapi og utvikling (Therapy and development)
2.4a Fjordlys og samhold for individer (FS1)
2.4b Fjordlys og samhold i familier (FS2)
2.4c Fjordlys og samhold i grupper (FS3)
2.4d Fjordlys og samhold i institusjoner (FS4)

Page 3: Aktuelt (Blog): this is our blog where we share knowledge and articles

Page 4: Kontakt (Contact): This is the contact form page. Contact form should constitute:
- Ditt navn (your name)
- E-post (your e-mail)
- Emne (subject)
- Melding (message/description)

Our project should also include suggestion for handheld units (iPhone, iPad).
Updates

We have both been traveling with work for a while, and then unfortunately both of us got sick on return, so we need a few more days to evaluate and choose design. Kind Regards Arvid & Margit

Target Market(s)

Focus on therapy, learning, mastery and growth for children and teenagers with special needs, within the family dynamics, or in a group setting.
OUR MARKETS:
Private market: individuals, families, groups and health industry institutions (with focus on learning, mastery, growth (as well as growing up) and psychiatry for children and teenagers with special difficulties and needs)
Public institutions: Government institutions, state institutions and municipality institutions (e.g. schools, municipality health service, hospitals) that serve the public (families with children and teenagers with special needs, and where learning, mastery, growth (as well as growing up) and potential psychiatry is an issue).

Number of Pages Required

4 page

Font styles to use
Sans Serif

Colors

Designer to choose colors to be used in the design.

Requirements
Must have
• The website must have 4 pages with roll down curtain menus (we have added a PDF with suggested structure, and headings, with sub menus - see attached PDF drawing.
• The web page must also use the added logo file - and make the web page work well with our logo.
• We would like the website to have a modern look and we would like the site to be associated with typical HIGH END TOP QUALITY private health institutions, but with a stronger focus on human beings (hands, faces etc), and not white coats and doctors. We are psychologists in the private market.
• For instance, if photos are being used - we tend to like "warm" almost art-like, "grainy" two-tone (e.g. sepia) photos to illustrate our focus. If designer can find such photos as part of design, it would be interesting to us. We would like a few photos like that integrated in the design.
• We also want a design suggestion for how the web page should look like and behave on handheld units (e.g. iPhone, iPad).
Nice to have
• If designer could find a number of suitable photos that matches the business idea and design requirements (see description above), that could follow website, that would be good.
• It could also be nice to have graphic symbols that denote the different pages/subpages (subjects)....
• HORSES: we sometimes use horses as a "tool" in therapy sessions. The horse is not necessarily used for riding, but for contact, communication and grooming. PHOTOS: we would like the designer to find an opportunity for using a photo reflecting this cooperation between therapist, child, teenager and horse. It is a bit up to the designer to find a way to do this... Since the horse is only a tool, among many other tools, it does not have to be much - but we want to try and see how it will work with a photo that also reflects this part of our business.

```html
<!DOCTYPE html>
<html lang="no">
<head>
<meta charset="utf-8">
<title>Tjenester – Fjordlys og Samhold</title>
<link href="https://fonts.googleapis.com/css2?family=Playfair+Display:wght@400;500;600;700&display=swap" rel="stylesheet">
<style>
  :root {
    --navy: #2c3b8f;
    --ink: #1f2a5c;
    --body: #4a4a4a;
    --muted: #8a8a8a;
    --green: #3cbf5a;
    --line: #d9dbe6;
    --white: #ffffff;
  }
  * { margin: 0; padding: 0; box-sizing: border-box; }
  html, body { width: 1200px; height: 2699px; overflow: hidden; background: var(--white); }
  body { position: relative; font-family: "Playfair Display", Georgia, serif; color: var(--body); }

  .site-header { position: absolute; top: 0; left: 0; width: 1200px; height: 165px; background: var(--white); box-shadow: 0 1px 3px rgba(0,0,0,.12); }
  .nav-link { position: absolute; top: 68px; font-size: 14px; font-weight: 600; color: var(--navy); text-decoration: none; }
  .nav-link.about { left: 124px; }
  .nav-link.services { left: 334px; }
  .nav-link.services svg { margin-left: 14px; vertical-align: middle; }
  .nav-link.news { left: 790px; }
  .nav-link.contact { left: 910px; }
  .brand { position: absolute; left: 0; width: 1200px; top: 66px; text-align: center; font-size: 22px; font-weight: 600; color: var(--navy); }
  .search-btn { position: absolute; left: 1031px; top: 55px; width: 46px; height: 46px; border: 1px solid var(--line); border-radius: 50%; display: flex; align-items: center; justify-content: center; }

  .hero { position: absolute; top: 165px; left: 0; width: 1200px; height: 416px;
    background: linear-gradient(100deg, #a88b66 0%, #b89470 30%, #c49a6a 55%, #a96a37 85%, #8e5226 100%); }
  .hero-title { position: absolute; right: 126px; top: 170px; font-size: 54px; font-weight: 600; color: var(--white); }
  .hero-sub { position: absolute; right: 126px; top: 245px; font-size: 20px; font-weight: 600; color: var(--green); }

  .service { position: absolute; left: 213px; width: 776px; }
  .service-head { display: flex; align-items: center; height: 36px; }
  .service-head svg { width: 30px; height: 30px; margin-right: 27px; }
  .service-title { font-size: 27px; font-weight: 700; color: var(--navy); letter-spacing: .3px; }
  .service p { font-size: 13.5px; line-height: 23.5px; margin-top: 18px; }
  .service p + p { margin-top: 16px; }

  .theme-cards { position: absolute; top: 1400px; left: 213px; display: flex; gap: 24px; }
  .theme-card { width: 242px; }
  .photo { display: block; }
  .theme-card .photo { width: 242px; height: 167px; }
  .theme-card h3 { font-size: 20.5px; font-weight: 600; color: var(--ink); text-align: center; margin-top: 22px; }
  .theme-card p { font-size: 11.5px; line-height: 21.7px; margin-top: 18px; }

  .therapy-item { position: absolute; display: flex; }
  .therapy-item .photo { width: 175px; height: 191px; flex: none; }
  .therapy-item .text { margin-left: 25px; width: 170px; padding-top: 10px; }
  .therapy-item h3 { font-size: 20.5px; line-height: 27px; font-weight: 600; color: var(--ink); }
  .therapy-item p { font-size: 11.5px; line-height: 21.7px; margin-top: 12px; }

  .site-footer { position: absolute; top: 2672px; left: 0; width: 1200px; text-align: center; font-size: 10px; color: var(--muted); }
</style>
</head>
<body>

<header class="site-header">
  <a class="nav-link about" href="#">Om Fjordlys og Samhold</a>
  <a class="nav-link services" href="#">Tjenester<svg width="11" height="7" viewBox="0 0 11 7"><path d="M1 1l4.5 4.5L10 1" fill="none" stroke="#2c3b8f" stroke-width="1"/></svg></a>
  <div class="brand">Fjordlys og Samhold</div>
  <a class="nav-link news" href="#">Aktuelt</a>
  <a class="nav-link contact" href="#">Kontakt</a>
  <div class="search-btn"><svg width="18" height="18" viewBox="0 0 18 18"><circle cx="7.5" cy="7.5" r="6" fill="none" stroke="#2c3b8f" stroke-width="1.3"/><path d="M12 12l5 5" stroke="#2c3b8f" stroke-width="1.3"/></svg></div>
</header>

<section class="hero" role="img" aria-label="Warm sepia photo of a young man looking out over misty mountains">
  <h1 class="hero-title">Tjenester</h1>
  <div class="hero-sub">Våre 5 Tjenesteområder</div>
</section>

<section class="service" style="top:683px">
  <div class="service-head">
    <svg viewBox="0 0 30 30"><circle cx="12" cy="12" r="10" fill="none" stroke="#2c3b8f" stroke-width="1.5"/><path d="M19.5 19.5l8 8" stroke="#2c3b8f" stroke-width="1.5"/></svg>
    <h2 class="service-title">UTREDNING</h2>
  </div>
  <p>Donec a condimentum quam, eu condimentum libero. Donec laoreet tellus libero, at mollis dui luctus et. Vestibulum egestas pulvinar metus, id scelerisque velit mollis in. Sed luctus porttitor nibh eget eleifend. Cras eu maximus ex. Donec rhoncus pharetra mi et ullamcorper. Maecenas commodo ipsum ac lobortis facilisis.</p>
</section>

<section class="service" style="top:905px">
  <div class="service-head">
    <svg viewBox="0 0 30 30"><path d="M15 4C8 4 3 8.5 3 14c0 3 1.5 5.6 4 7.4L5.5 27l6-3.4c1.1.3 2.3.4 3.5.4 7 0 12-4.5 12-10S22 4 15 4z" fill="none" stroke="#2c3b8f" stroke-width="1.5"/></svg>
    <h2 class="service-title">RÅDGIVNING</h2>
  </div>
  <p>Morbi sollicitudin nibh eget ipsum congue pellentesque. Nam gravida luctus lacus, elementum molestie elit fringilla eu. Quisque rutrum, ante a interdum bibendum, risus ligula mollis dolor, quis tincidunt odio enim non lorem. Nulla ac diam tempor, ullamcorper leo in, tempus nisi. Aliquam convallis ligula eu est efficitur, hendrerit consectetur urna fermentum.</p>
  <p>Proin egestas tellus elit. Phasellus vulputate, sem quis dictum bibendum, magna ligula sodales nibh, vel interdum urna nisl id justo. Sed tortor tortor, molestie at tempus et, suscipit at odio.</p>
</section>

<section class="service" style="top:1191px">
  <div class="service-head">
    <svg viewBox="0 0 30 30"><path d="M16 5H3v22h22V14" fill="none" stroke="#2c3b8f" stroke-width="1.5"/><path d="M12 18l1-4L24 3l3 3-11 11z" fill="none" stroke="#2c3b8f" stroke-width="1.5"/></svg>
    <h2 class="service-title">KURS OG WORKSHOPS</h2>
  </div>
  <p>Proin et ante quis sem lacinia tristique et nec justo. Proin lobortis ex eu porttitor cursus. Suspendisse potenti. Donec tristique dapibus magna, nec porta diam. Donec tincidunt justo eget semper rutrum. Curabitur porta sapien ac tempus vehicula. Nunc pretium venenatis turpis, eu posuere mi vehicula nec. Proin euismod venenatis sollicitudin. Maecenas bibendum urna velit, eget iaculis ligula porta in.</p>
</section>

<div class="theme-cards">
  <article class="theme-card">
    <div class="photo" role="img" aria-label="Sepia photo of a person meditating on a hilltop" style="background:linear-gradient(180deg,#b7a48c 0%,#9a8468 50%,#6e5538 100%)"></div>
    <h3>Fjordlys og Samhold Tema 1</h3>
    <p>Proin et ante quis sem lacinia tristique et nec justo. Proin lobortis ex eu porttitor cursus. Suspendisse potenti. Donec tristique dapibus magna, nec porta diam. Donec tincidunt justo eget semper rutrum. Curabitur porta sapien ac tempus vehicula.</p>
  </article>
  <article class="theme-card">
    <div class="photo" role="img" aria-label="Warm photo of two children leaning on a tree" style="background:linear-gradient(90deg,#a0866b 0%,#8a6a44 50%,#4a3a2a 100%)"></div>
    <h3>Fjordlys og Samhold Tema 2</h3>
    <p>Proin et ante quis sem lacinia tristique et nec justo. Proin lobortis ex eu porttitor cursus. Suspendisse potenti. Donec tristique dapibus magna, nec porta diam. Donec tincidunt justo eget semper rutrum. Curabitur porta sapien ac tempus vehicula.</p>
  </article>
  <article class="theme-card">
    <div class="photo" role="img" aria-label="Open hands holding a small yellow flower" style="background:radial-gradient(circle at 50% 50%,#c99a78 0%,#7a5a3e 50%,#3a2a1e 100%)"></div>
    <h3>Fjordlys og Samhold Tema 3</h3>
    <p>Proin et ante quis sem lacinia tristique et nec justo. Proin lobortis ex eu porttitor cursus. Suspendisse potenti. Donec tristique dapibus magna, nec porta diam. Donec tincidunt justo eget semper rutrum. Curabitur porta sapien ac tempus vehicula.</p>
  </article>
</div>

<section class="service" style="top:1855px">
  <div class="service-head">
    <svg viewBox="0 0 30 30"><circle cx="14" cy="9" r="6" fill="none" stroke="#2c3b8f" stroke-width="1.5"/><path d="M3 28c0-6 4.5-10 11-10 2 0 3.5.3 5 1" fill="none" stroke="#2c3b8f" stroke-width="1.5"/><path d="M24 28l-4-4a2.2 2.2 0 013.9-2 2.2 2.2 0 013.9 2z" fill="none" stroke="#2c3b8f" stroke-width="1.4"/></svg>
    <h2 class="service-title">TERAPI OG UTVIKLING</h2>
  </div>
  <p>Nam vitae lacus ultricies erat maximus condimentum. Donec vehicula nulla id blandit rutrum. Praesent sapien mauris, dictum vitae justo eget, cursus ullamcorper urna. Integer blandit, sem eget elementum commodo, justo purus fermentum ipsum, ut molestie sem erat et lectus. Mauris orci diam, consectetur eget lacus quis, semper scelerisque nisl. Pellentesque risus nunc, facilisis sed scelerisque in, malesuada eu lectus.</p>
</section>

<article class="therapy-item" style="top:2064px;left:213px">
  <div class="photo" role="img" aria-label="Person seen from behind looking over a calm lake" style="background:linear-gradient(180deg,#b7a6a0 0%,#8f8078 45%,#4a3c36 100%)"></div>
  <div class="text">
    <h3>Fjordlys og Samhold for Individer</h3>
    <p>Proin et ante quis sem lacinia tristique et nec justo. Proin lobortis ex eu porttitor cursus. Suspendisse potenti. Donec tristique dapibus magna.</p>
  </div>
</article>
<article class="therapy-item" style="top:2064px;left:621px">
  <div class="photo" role="img" aria-label="Family sitting together in a sunlit forest" style="background:linear-gradient(180deg,#c8c4a8 0%,#9a9478 50%,#4e4a34 100%)"></div>
  <div class="text">
    <h3>Fjordlys og Samhold i Familier</h3>
    <p>Proin et ante quis sem lacinia tristique et nec justo. Proin lobortis ex eu porttitor cursus. Suspendisse potenti. Donec tristique dapibus magna.</p>
  </div>
</article>
<article class="therapy-item" style="top:2295px;left:213px">
  <div class="photo" role="img" aria-label="Group of friends embracing at sunset" style="background:linear-gradient(180deg,#f0d8c4 0%,#d8a070 55%,#8a5028 100%)"></div>
  <div class="text">
    <h3>Fjordlys og Samhold i Grupper</h3>
    <p>Proin et ante quis sem lacinia tristique et nec justo. Proin lobortis ex eu porttitor cursus. Suspendisse potenti. Donec tristique dapibus magna.</p>
  </div>
</article>
<article class="therapy-item" style="top:2295px;left:621px">
  <div class="photo" role="img" aria-label="Colleagues talking together in an office" style="background:linear-gradient(180deg,#c8c0b6 0%,#8a7a66 50%,#4a3e32 100%)"></div>
  <div class="text">
    <h3>Fjordlys og Samhold i Institusjoner</h3>
    <p>Proin et ante quis sem lacinia tristique et nec justo. Proin lobortis ex eu porttitor cursus. Suspendisse potenti. Donec tristique dapibus magna.</p>
  </div>
</article>

<footer class="site-footer">©2020 Fjordlys og Samhold. All Rights Reserved.</footer>

</body>
</html>
```